Lena Corvell Business Card

I need a business card that reflects my current website: itslenacorvell.example and screenshot attached. If we keep the color scheme of the site and sample card below that would be ideal. The business card should include the information on the attached sample cards.

Industry/Entity Type

Business

```html
<!DOCTYPE html>
<html lang="en">
<head>
<meta charset="utf-8">
<title>Lena Corvell Business Card</title>
<link rel="stylesheet" href="https://fonts.googleapis.com/css2?family=Source+Sans+3:wght@400;600;700&display=swap">
<style>
  :root {
    --page-bg: #d9d9d9;
    --card-dark: #252223;
    --card-mid: #3a3738;
    --card-light: #7a7879;
    --tab-white: #ffffff;
    --ink-dark: #1c1a1b;
    --name-white: #ffffff;
    --tagline-grey: #b9b9b9;
    --contact-grey: #dcdcdc;
  }
  * { margin: 0; padding: 0; box-sizing: border-box; }
  html, body {
    width: 1200px;
    height: 900px;
    overflow: hidden;
    background: var(--page-bg);
    font-family: "Source Sans 3", "Myriad Pro", sans-serif;
  }
  .business-card {
    position: absolute;
    left: 100px;
    top: 164px;
    width: 1000px;
    height: 572px;
    background: var(--card-dark);
    overflow: hidden;
    box-shadow: 0 10px 30px rgba(0,0,0,0.25);
  }
  .card-sheen {
    position: absolute;
    inset: 0;
    width: 100%;
    height: 100%;
  }
  .card-name {
    position: absolute;
    right: 62px;
    top: 46px;
    font-size: 44px;
    font-weight: 700;
    color: var(--name-white);
    letter-spacing: 0.5px;
  }
  .card-tagline {
    position: absolute;
    right: 62px;
    top: 104px;
    font-size: 22px;
    font-weight: 400;
    color: var(--tagline-grey);
    white-space: nowrap;
  }
  .name-tab {
    position: absolute;
    left: 0;
    top: 268px;
    width: 350px;
    height: 92px;
    background: var(--tab-white);
    border-radius: 0 16px 16px 0;
    display: flex;
    align-items: center;
    justify-content: center;
  }
  .name-tab-text {
    font-size: 34px;
    font-weight: 400;
    color: var(--ink-dark);
  }
  .contact-list {
    position: absolute;
    right: 62px;
    top: 300px;
    list-style: none;
    text-align: right;
    font-size: 27px;
    line-height: 38px;
    color: var(--contact-grey);
  }
</style>
</head>
<body>
  <main class="business-card">
    <svg class="card-sheen" viewBox="0 0 1000 572" preserveAspectRatio="none" aria-hidden="true">
      <defs>
        <linearGradient id="sheenGradient" x1="0" y1="0" x2="1" y2="0.4">
          <stop offset="0" stop-color="var(--card-mid)"/>
          <stop offset="0.35" stop-color="var(--card-light)"/>
          <stop offset="0.75" stop-color="var(--card-mid)"/>
          <stop offset="1" stop-color="var(--card-dark)"/>
        </linearGradient>
      </defs>
      <path d="M470 0 L1000 0 L1000 572 L400 572 C420 470 440 380 430 300 C425 200 455 90 470 0 Z" fill="url(#sheenGradient)"/>
    </svg>

    <h1 class="card-name">LENA CORVELL</h1>
    <p class="card-tagline">Brand Curator | Digital Storyteller | Social Entrpreneur</p>

    <div class="name-tab">
      <span class="name-tab-text">Lena Corvell</span>
    </div>

    <ul class="contact-list">
      <li>me@lenacorvell.example</li>
      <li>555.014.2290</li>
      <li>[fb] | [t.] | [ig] @itslenacorvell</li>
      <li>www.itslenacorvell.example</li>
    </ul>
  </main>
</body>
</html>
```